Startup Technology Consulting Firm in NYC Needs A Website

I need a website built for my startup technology consulting company Brightmoor Systems Collective. We offer a unique white glove service that provides end to end technology support. I want to stand out above the rest. We are small firm but are very dedicated which where we derive our name from BSC primarily offers
end to end technology advisory services to small businesses lacking their own IT staff. We offer top notch white glove and our customer service and satisfaction is exceed by no one.

Below are some of what we provide our clients

Strategic IT Planning
Business Continuity Planning/Disaster Recovery
Cloud Computing\DataCenter Solutions
Server Infrastructure/Networking
Virtualization Technologies
Project Management

Our Technology Advisors hold many certifications from Quillora & Tessfold. We are also Quillora Partners

I have attached my logo (preview design) As soon as I ge the final images I will upload.

Reason: want to give more time to submit designs

Industry/Entity Type

Information Technology

Coding

Coded - Design and coding required

Number of Pages Required

1 page

Font styles to use
Sans Serif

Requirements
Must have
• Attract Target Market. The site should bleed the company vision
• DEDICATION everything about the site should show this
• Layout the Benefits of our offerings
• Links to my social media
• Links to dircct my client's for remote support

```html
<!DOCTYPE html>
<html lang="en">
<head>
<meta charset="utf-8">
<title>Brightmoor Systems Collective</title>
<link rel="stylesheet" href="https://fonts.googleapis.com/css2?family=Open+Sans:wght@300;400;600;700&display=swap">
<style>
:root{
  --blue:#1f6fbe;
  --blue-dark:#0c63ad;
  --green:#7cbb2f;
  --ink:#333a40;
  --muted:#5c6670;
  --vision:#d5e7f6;
  --white:#ffffff;
}
*{box-sizing:border-box;margin:0;padding:0}
html,body{width:1200px;height:1200px;overflow:hidden;background:var(--white)}
body{font-family:"Open Sans",Arial,sans-serif;color:var(--ink);position:relative}
.page{position:absolute;left:394px;top:0;width:514px;height:1500px;transform:scale(.8);transform-origin:0 0;background:var(--white);overflow:hidden}
.abs{position:absolute}
.hl{color:var(--blue)}
.btn{position:absolute;background:var(--green);color:var(--white);font-weight:600;text-transform:uppercase;display:flex;align-items:center;justify-content:center;white-space:nowrap;box-shadow:0 2px 2px rgba(0,0,0,.15)}
/* header */
.brand{left:22px;top:32px;display:flex;align-items:center;gap:5px;white-space:nowrap}
.brand-mark{width:10px;height:10px;border-radius:50%;background:var(--blue)}
.brand-name{font-size:7.5px;font-weight:600;color:var(--blue);letter-spacing:.2px}
.call{right:27px;top:5px;font-size:6.5px;color:var(--muted);white-space:nowrap}
.call b{color:var(--blue)}
.social{display:flex;gap:4px}
.social span{width:14px;height:14px;border-radius:50%;border:1px solid #7a9cc4;display:block}
.head-social{left:427px;top:20px}
.nav-item{position:absolute;top:42px;font-size:6.5px;color:#444;white-space:nowrap;text-decoration:none;padding-bottom:4px}
.nav-item.on{color:var(--blue);border-bottom:1px solid var(--blue)}
/* hero */
.hero{left:0;top:55px;width:514px;height:216px;background:linear-gradient(100deg,#eef3f6 0%,#dfe9ef 40%,#aac1d4 70%,#8aa9c4 100%)}
.hero-visual{left:222px;top:0;width:292px;height:216px;background:radial-gradient(ellipse at 45% 50%,#2a73c0 0%,#3f80c2 35%,rgba(138,169,196,.6) 70%,rgba(138,169,196,0) 100%)}
.hero-title{left:22px;top:44px;font-size:16px;font-weight:300;line-height:25px;color:#2b3540;letter-spacing:.1px;white-space:nowrap}
.hero-btn{left:22px;top:151px;width:151px;height:26px;font-size:8px}
/* welcome */
.welcome-title{left:22px;top:307px;font-size:18px;font-weight:300;color:#222;white-space:nowrap}
.welcome-copy{left:22px;top:332px;width:310px;font-size:6.3px;line-height:10.8px;color:var(--ink)}
.read-btn{left:22px;top:436px;width:61px;height:18px;font-size:7px;text-transform:none;font-weight:400}
.vision{left:343px;top:311px;width:149px;height:142px;background:var(--vision);border-bottom:2px solid #b8d2e8;text-align:center;padding:18px 10px 0}
.vision h3{font-size:11px;font-weight:400;color:var(--blue);margin-bottom:4px}
.vision p{font-size:6.2px;line-height:12px;color:var(--ink)}
/* services */
.services{left:0;top:490px;width:514px;height:260px;background:linear-gradient(180deg,#e3edf3 0%,#f4f8fa 45%,#dbe8ef 100%)}
.sec-title{position:absolute;left:0;width:514px;text-align:center;font-size:18px;font-weight:300;color:#222;white-space:nowrap}
.svc{position:absolute;width:160px;text-align:center;font-size:7px;line-height:11px;color:#3c4550}
.svc svg{display:block;margin:0 auto 5px}
/* benefits */
.ben-sub{left:50px;top:801px;width:414px;text-align:center;font-size:6.3px;line-height:11px;color:var(--ink)}
.ben-list{left:22px;top:835px;width:460px;list-style:none;font-size:6.3px;line-height:11px}
.ben-list li{position:relative;padding-left:16px;height:25px}
.ben-list li svg{position:absolute;left:0;top:2px}
.support-btn{font-size:9px}
/* certifications */
.certs{left:0;top:1017px;width:514px;height:246px;background:radial-gradient(ellipse at 60% 50%,#ffffff 0%,#eef4f8 55%,#d6e6f0 100%)}
.badge{position:absolute;width:70px;height:50px;border-radius:3px;background:#c9d9e6}
.support-title{left:0;top:1292px;width:514px;text-align:center;font-size:15px;font-weight:300;color:#3a434b;white-space:nowrap}
/* footer */
.footer{left:0;top:1383px;width:514px;height:117px;background:var(--blue-dark);color:var(--white)}
.fcol{position:absolute;top:14px;font-size:6px;line-height:12.7px;white-space:nowrap}
.fcol h4{font-size:7px;font-weight:600;margin-bottom:1px;line-height:12px}
.foot-social{left:263px;top:70px}
.foot-social span{border-color:var(--white)}
.copy{right:38px;top:100px;font-size:5.5px;position:absolute;white-space:nowrap}
</style>
</head>
<body>
<div class="page">
  <!-- header -->
  <div class="abs brand"><span class="brand-mark"></span><span class="brand-name">Brightmoor Systems Collective</span></div>
  <div class="abs call">Call Us: <b>555-014-(2290)</b></div>
  <div class="abs social head-social" aria-label="Social media links"><span></span><span></span><span></span></div>
  <nav>
    <a class="nav-item on" style="left:232px">Home</a>
    <a class="nav-item" style="left:276px">About Us</a>
    <a class="nav-item" style="left:328px">Our Services</a>
    <a class="nav-item" style="left:391px">Our Benefits</a>
    <a class="nav-item" style="left:454px">Contact Us</a>
  </nav>

  <!-- hero -->
  <section class="abs hero">
    <div class="abs hero-visual" role="img" aria-label="Hand touching a honeycomb of blue service hexagons: IT Planning, Virtualization Technologies, Server Infrastructure, Business Continuity Planning, Cloud Computing, Project Management"></div>
    <h1 class="abs hero-title">WE OFFER END TO END<br>TECHNOLOGY ADVISORY<br>SERVICES TO SMALL<br>BUSINESSES</h1>
    <div class="btn hero-btn">Get Started Now &nbsp;»</div>
  </section>

  <!-- welcome -->
  <h2 class="abs welcome-title">WELCOME TO <span class="hl">BSC</span></h2>
  <p class="abs welcome-copy">Lorem ipsum dolor sit amet, consectetur adipiscing elit. Donec venenatis vehicula rhoncus. Suspendisse ultricies posuere euismod. Quisque rutrum sollicitudin faucibus. Ut eu enim ac augue ultricies bibendum. Proin eget lectus diam, id feugiat ante. Nam lobortis magna sed est posuere eget ornare augue facilisis. Cras nulla tellus, eleifend eu interdum at, pharetra ut felis. Donec semper, augue eu venenatis construr, ipsum nisl placerat lorem, et eleifend enim odio vitae odio. Proin ac tortor malesuada lacus rhoncus vehicula. Donec dui dolor, rutrum rutrum sagittis quis, mattis in nulla. Pellentesque elementum enim id turpis consectetur laoreet. Vestibulum tempus condimentum lorem, quis bibendum mi eleifend eu. Nullam eros ante, ultrices vitae malesuada sed, sollicitudin vitae tellus. Phasellus congue egestas nunc, quis dapibus diam gravida a.</p>
  <div class="btn read-btn">Read More</div>
  <aside class="abs vision">
    <h3>OUR VISION</h3>
    <p>Lorem ipsum dolor sit amet, consectetur adiscing elit. Donec venenatis vehicula roncus. Sspendisse ultricies posuere euis-mod. Quisque rutrum sollicitudin fauci-bus. Ut eu enim ac augue ultricies bibdum. Proin eget lectus diam, id feugiat ante.</p>
  </aside>

  <!-- services -->
  <section class="abs services">
    <h2 class="sec-title" style="top:30px">OUR <span class="hl">SERVICES</span></h2>
    <div class="svc" style="left:16px;top:72px">
      <svg width="48" height="48" viewBox="0 0 48 48" fill="none" stroke="var(--blue)" stroke-width="1.3"><circle cx="24" cy="24" r="23" fill="#fff"/><rect x="18" y="13" width="12" height="20" rx="1.5"/><path d="M21 22l3 3 4-6"/></svg>
      Strategic IT Planning</div>
    <div class="svc" style="left:177px;top:72px">
      <svg width="48" height="48" viewBox="0 0 48 48" fill="none" stroke="var(--blue)" stroke-width="1.3"><circle cx="24" cy="24" r="23" fill="#fff"/><circle cx="24" cy="17" r="3"/><circle cx="16" cy="27" r="3"/><circle cx="32" cy="27" r="3"/><path d="M11 35c1-4 9-4 10 0M27 35c1-4 9-4 10 0"/></svg>
      Business Continuity<br>Planning/Disaster Recovery</div>
    <div class="svc" style="left:337px;top:72px">
      <svg width="48" height="48" viewBox="0 0 48 48" fill="none" stroke="var(--blue)" stroke-width="1.3"><circle cx="24" cy="24" r="23" fill="#fff"/><path d="M15 25a6 6 0 0 1 4-10 7 7 0 0 1 13 2 5 5 0 0 1 1 9z"/><rect x="18" y="27" width="12" height="8"/></svg>
      Cloud Computing\DataCenter<br>Solutions</div>
    <div class="svc" style="left:16px;top:160px">
      <svg width="48" height="48" viewBox="0 0 48 48" fill="none" stroke="var(--blue)" stroke-width="1.3"><circle cx="24" cy="24" r="23" fill="#fff"/><rect x="20" y="12" width="8" height="7"/><path d="M24 19v5M15 24h18M15 24v4M33 24v4M24 24v4"/><rect x="12" y="28" width="6" height="6"/><rect x="21" y="28" width="6" height="6"/><rect x="30" y="28" width="6" height="6"/></svg>
      Server Infrastructure/Networking</div>
    <div class="svc" style="left:177px;top:160px">
      <svg width="48" height="48" viewBox="0 0 48 48" fill="none" stroke="var(--blue)" stroke-width="1.3"><circle cx="24" cy="24" r="23" fill="#fff"/><path d="M22 20a4 4 0 0 1 3-7 5 5 0 0 1 9 2 3 3 0 0 1 0 5z"/><rect x="13" y="25" width="9" height="8"/><rect x="27" y="25" width="8" height="10"/><path d="M22 29h5"/></svg>
      Virtualization Technologies</div>
    <div class="svc" style="left:337px;top:160px">
      <svg width="48" height="48" viewBox="0 0 48 48" fill="var(--blue)" stroke="var(--blue)" stroke-width="1.3"><circle cx="24" cy="24" r="23" fill="#fff"/><circle cx="24" cy="18" r="4"/><circle cx="15" cy="22" r="3"/><circle cx="33" cy="22" r="3"/><path d="M16 34c0-6 16-6 16 0zM9 32c0-5 8-5 9-2M39 32c0-5-8-5-9-2"/></svg>
      Project Management</div>
  </section>

  <!-- benefits -->
  <h2 class="sec-title" style="top:776px">BENEFITS OF <span class="hl">OUR OFFERINGS</span></h2>
  <p class="abs ben-sub">Lorem ipsum dolor sit amet, consectetur adipiscing elit. Donec venenatis vehicula rhoncus. Sspendisse ultricies posuere euismod.<br>Quisque rutrum sollicitudin faucibus.</p>
  <ul class="abs ben-list">
    <li><svg width="14" height="6" viewBox="0 0 14 6" fill="var(--blue)"><rect x="0" y="2" width="1" height="2"/><rect x="2" y="2" width="1" height="2"/><rect x="4" y="2" width="4" height="2"/><path d="M8 0l5 3-5 3z"/></svg>Lorem ipsum dolor sit amet, consectetur adipiscing elit. Donec venenatis vehicula rhoncus. Sspendisse ultricies posuere euismod. Quisque rutrum sollicitudin faucibus.</li>
    <li><svg width="14" height="6" viewBox="0 0 14 6" fill="var(--blue)"><rect x="0" y="2" width="1" height="2"/><rect x="2" y="2" width="1" height="2"/><rect x="4" y="2" width="4" height="2"/><path d="M8 0l5 3-5 3z"/></svg>Lorem ipsum dolor sit amet, consectetur adipiscing elit. Donec venenatis vehicula rhoncus. Sspendisse ultricies posuere euismod. Quisque rutrum sollicitudin faucibus.</li>
    <li><svg width="14" height="6" viewBox="0 0 14 6" fill="var(--blue)"><rect x="0" y="2" width="1" height="2"/><rect x="2" y="2" width="1" height="2"/><rect x="4" y="2" width="4" height="2"/><path d="M8 0l5 3-5 3z"/></svg>Lorem ipsum dolor sit amet, consectetur adipiscing elit. Donec venenatis vehicula rhoncus. Sspendisse ultricies posuere euismod. Quisque rutrum sollicitudin faucibus.</li>
    <li><svg width="14" height="6" viewBox="0 0 14 6" fill="var(--blue)"><rect x="0" y="2" width="1" height="2"/><rect x="2" y="2" width="1" height="2"/><rect x="4" y="2" width="4" height="2"/><path d="M8 0l5 3-5 3z"/></svg>Lorem ipsum dolor sit amet, consectetur adipiscing elit. Donec venenatis vehicula rhoncus. Sspendisse ultricies posuere euismod. Quisque rutrum sollicitudin faucibus.</li>
    <li><svg width="14" height="6" viewBox="0 0 14 6" fill="var(--blue)"><rect x="0" y="2" width="1" height="2"/><rect x="2" y="2" width="1" height="2"/><rect x="4" y="2" width="4" height="2"/><path d="M8 0l5 3-5 3z"/></svg>Lorem ipsum dolor sit amet, consectetur adipiscing elit. Donec venenatis vehicula rhoncus. Sspendisse ultricies posuere euismod. Quisque rutrum sollicitudin faucibus.</li>
  </ul>
  <div class="btn support-btn" style="left:158px;top:969px;width:198px;height:26px">Click Here For Remote Support &nbsp;»</div>

  <!-- certifications -->
  <section class="abs certs">
    <h2 class="sec-title" style="top:28px;font-size:17px">OUR CERTIFICATIONS <span class="hl">AND AFFILIATIONS</span></h2>
    <svg class="abs" style="left:0;top:0" width="514" height="246" fill="none" stroke="#8a97a3" stroke-width=".7" stroke-dasharray="2 2">
      <line x1="176" y1="60" x2="176" y2="220"/><line x1="338" y1="60" x2="338" y2="220"/><line x1="44" y1="144" x2="470" y2="144"/>
    </svg>
    <div class="badge" style="left:62px;top:83px" role="img" aria-label="Quillora certification badge"></div>
    <div class="badge" style="left:222px;top:83px" role="img" aria-label="Quillora certification badge"></div>
    <div class="badge" style="left:383px;top:83px" role="img" aria-label="Tessfold certification badge"></div>
    <div class="badge" style="left:62px;top:156px" role="img" aria-label="Quillora certification badge"></div>
    <div class="badge" style="left:222px;top:156px" role="img" aria-label="Quillora certification badge"></div>
  </section>

  <!-- support -->
  <h2 class="abs support-title">FOR IMMIDIATE SUPPORT ASSISTANCE</h2>
  <div class="btn support-btn" style="left:155px;top:1321px;width:204px;height:25px">Click Here For Remote Support &nbsp;»</div>

  <!-- footer -->
  <footer class="abs footer">
    <div class="fcol" style="left:22px"><h4>Quick Links</h4>› Home<br>› About Us<br>› Our Services<br>› Our Benefits<br>› Contact Us</div>
    <div class="fcol" style="left:102px"><h4>Services Offered</h4>› Strategic IT Planning<br>› Business Continuity Planning/Disaster Recovery<br>› Cloud Computing\DataCenter Solutions<br>› Server Infrastructure/Networking<br>› Virtualization Technologies<br>› Project Management</div>
    <div class="fcol" style="left:263px;line-height:10px"><h4>Contact Us</h4>Address Will Come Here<br>Address Will Come Here<br>Ph No. <b>555-014-(2290)</b><br>Email: info@brightmoorsystems.com</div>
    <div class="abs social foot-social" aria-label="Social media links"><span></span><span></span><span></span></div>
    <div class="copy">Copyright © 2015. Brightmoor Systems Collective. All Rights Reserved.</div>
  </footer>
</div>
</body>
</html>
```